Australian Legal Practice would like a Web Design

I need a web design for a newly established law practice operating as Brindell Legal.

I would like the business to have an internet presence (via a website) essentially for the purpose of marketing and advertising. As the business grows (hopefully) I may be interested in providing general legal information as a means of establishing goodwill in the community and a easy and user friends contact method through the website.

The essence of the business is personal legal service based on local knowledge and therefore i want the website to present a picture of friendly professionalism, but mostly i want people who to be able to find the contact details of the business

I would like to have a map of the office location, and photos of the front of the office, the staff (me at the moment) and picture of law themed items and featuring the Brindell Legal logo.

The areas of law which Brindell Legal practises in are as follows:

commercial law
business sale and purchases
leases
conveyancing and property law
wills and estates
powers of attorney
general legal advice
succession planning
Updates

Target Market(s)

Potential and existing clients of the firm
Other law firms
Associated stakeholders, i.e. Banks and real estate agents

Industry/Entity Type

Law Firm

Coding

Coded - Design and coding required

Number of Pages Required

2 page

Font styles to use
Sans Serif

Colors
85acd3
33a6d7
0456a4

Requirements
Must have
• Brindell Legal logo
• Map of the office location
• Picture of Ross Kedwick (principal solicitor)
• Picture of the office
• Areas of Practice
• Address of office
• email address: ross.kedwick@brindelllegal-example.com.au
• Physical address: 17 Pellow Road, Hamilton VIC 3300
• Phone number: (03) 5598 4731
• Facsimile number: (03) 5598 4706
• Space for a brief description of the firm and its competitive advantage
• Bar Guild Logo
• Links to the Bar Guild of Victoria
• Link to the practitioner oversight Council
Nice to have
• coded to wordpress format

```html
<!DOCTYPE html>
<html lang="en">
<head>
<meta charset="utf-8">
<title>Brindell Legal – Hamilton Law Practice</title>
<link rel="stylesheet" href="https://fonts.googleapis.com/css2?family=Cinzel:wght@400;700&family=Open+Sans:wght@400;600;700&display=swap">
<style>
:root{
  --navy:#0456a4;
  --navy-deep:#0a2a52;
  --footer:#0c1b33;
  --footer-strip:#081326;
  --sky:#33a6d7;
  --powder:#85acd3;
  --ink:#2b2f36;
  --muted:#6b7280;
  --panel:#eef3f8;
  --white:#ffffff;
}
*{box-sizing:border-box;margin:0;padding:0}
html,body{width:878px;height:1200px;overflow:hidden}
body{font-family:"Open Sans",Arial,sans-serif;color:var(--ink);background:var(--white);position:relative}
.wrap{width:680px;margin:0 auto;position:relative}

/* header */
.site-header{height:80px}
.site-header .wrap{display:flex;justify-content:space-between;align-items:center;height:80px}
.brand{display:flex;align-items:center;gap:10px;font-family:"Cinzel",Georgia,serif;font-weight:700;font-size:26px;color:var(--navy);letter-spacing:1px}
.brand-mark{width:14px;height:14px;background:var(--navy)}
.header-contact{text-align:right;font-size:11px;color:var(--navy);line-height:20px}
.header-contact .phone{font-size:14px;font-weight:600}
.header-contact svg{vertical-align:-2px;margin-right:5px}

/* nav */
.main-nav{height:38px;background:var(--navy-deep)}
.main-nav ul{list-style:none;display:flex;width:680px;margin:0 auto;height:38px}
.main-nav li{font-family:"Cinzel",Georgia,serif;font-size:12px;color:var(--white);padding:0 22px;line-height:38px;letter-spacing:.5px}
.main-nav li.active{background:var(--sky)}

/* hero */
.hero{height:287px;position:relative;background:linear-gradient(100deg,#5a3a22 0%,#8a6240 28%,#c9c3b8 55%,#e8ecef 75%,#b9c4cf 100%)}
.hero-arrow{position:absolute;top:126px;width:30px;height:34px;display:flex;align-items:center;justify-content:center}
.hero-arrow.prev{left:16px}
.hero-arrow.next{right:16px}

/* tagline */
.tagline{margin:16px auto 0;width:680px;height:46px;border-top:1px solid #e3e6ea;box-shadow:0 8px 10px -6px rgba(0,0,0,.35);text-align:center;font-family:"Cinzel",Georgia,serif;font-weight:700;font-size:21px;line-height:46px;color:#3a3f47;letter-spacing:1px}

/* welcome & areas */
.intro{display:flex;gap:30px;margin-top:34px}
.section-title{font-family:"Cinzel",Georgia,serif;font-size:14px;color:var(--ink);padding-bottom:6px;border-bottom:1px solid #d7dce2;margin-bottom:12px;letter-spacing:.5px}
.section-title span{color:var(--navy)}
.welcome{flex:0 0 390px}
.welcome-body{display:flex;gap:14px}
.portrait{flex:0 0 112px;height:150px;background:linear-gradient(180deg,#dfe5ec 0%,#9aa8b8 55%,#2f3a4a 100%)}
.welcome-text p{font-size:10px;line-height:15px;color:var(--muted)}
.read-more{display:inline-block;margin-top:10px;font-size:10px;color:var(--navy);border:1px solid #cfd6de;padding:2px 8px}
.areas{flex:1;background:var(--panel);border:1px solid #d7dfe8;padding:10px 14px}
.areas ul{list-style:none}
.areas li{font-size:10px;line-height:17px;color:var(--ink);padding-left:12px;position:relative}
.areas li::before{content:"";position:absolute;left:0;top:7px;width:4px;height:4px;background:var(--sky)}

/* why choose */
.why{position:absolute;left:0;top:725px;width:878px;height:245px;background:var(--sky);color:var(--white);text-align:center}
.why-notch{position:absolute;left:427px;top:0}
.why h2{font-family:"Cinzel",Georgia,serif;font-weight:400;font-size:20px;padding-top:30px;letter-spacing:1px}
.why .lead{width:640px;margin:14px auto 0;font-size:10.5px;line-height:16px;font-style:italic}
.why-points{display:flex;width:640px;margin:16px auto 0;text-align:left;gap:24px}
.why-points ul{list-style:none;flex:1}
.why-points li{font-size:10px;line-height:19px;padding-left:16px;position:relative}
.why-points svg{position:absolute;left:0;top:5px}
.why .read-more{border-color:rgba(255,255,255,.6);color:var(--white);margin-top:14px}

/* footer */
.site-footer{position:absolute;left:0;top:970px;width:878px;height:200px;background:var(--footer);color:#c8d2de}
.footer-cols{display:flex;gap:26px;padding-top:22px}
.footer-col h3{font-family:"Cinzel",Georgia,serif;font-weight:400;font-size:12px;color:var(--white);letter-spacing:.5px;padding-bottom:6px;border-bottom:1px solid #2a3a55;margin-bottom:8px}
.footer-col.links{width:130px}
.footer-col.contact{width:180px}
.footer-col.map{width:170px}
.footer-col.badges{width:120px;padding-top:6px}
.footer-col ul{list-style:none}
.footer-col li,.footer-col p{font-size:9.5px;line-height:16px}
.map-area{width:170px;height:110px;background:linear-gradient(135deg,#e9ecef,#cfd7df)}
.badge{width:100px;height:48px;margin-bottom:12px}
.badge.guild{background:var(--white)}
.badge.council{background:#6b3d8f}
.copyright{position:absolute;left:0;top:1170px;width:878px;height:30px;background:var(--footer-strip);color:#8fa0b5;font-size:9px;text-align:center;line-height:30px;letter-spacing:.5px}
</style>
</head>
<body>

<header class="site-header">
  <div class="wrap">
    <div class="brand"><span class="brand-mark"></span>Brindell Legal</div>
    <div class="header-contact">
      <div><svg width="12" height="9" viewBox="0 0 12 9"><rect x=".5" y=".5" width="11" height="8" fill="none" stroke="#0456a4"/><path d="M.5 .5 6 5l5.5-4.5" fill="none" stroke="#0456a4"/></svg>practice@brindelllegal-example.com.au</div>
      <div class="phone"><svg width="12" height="12" viewBox="0 0 12 12"><path d="M3 1 5 3.5 4 5c.8 1.4 1.6 2.2 3 3l1.5-1L11 9l-1 2C5 11 1 7 1 2z" fill="#0456a4"/></svg>(03) 5598 4706</div>
    </div>
  </div>
</header>

<nav class="main-nav">
  <ul>
    <li class="active">Home</li>
    <li>About Us</li>
    <li>Why Choose Us</li>
    <li>Areas of Practice</li>
    <li>Contact Us</li>
  </ul>
</nav>

<section class="hero" role="img" aria-label="Slideshow photo of a wooden judge's gavel beside legal documents">
  <div class="hero-arrow prev"><svg width="14" height="22" viewBox="0 0 14 22"><path d="M12 2 3 11l9 9" fill="none" stroke="#fff" stroke-width="3"/></svg></div>
  <div class="hero-arrow next"><svg width="14" height="22" viewBox="0 0 14 22"><path d="M2 2l9 9-9 9" fill="none" stroke="#fff" stroke-width="3"/></svg></div>
</section>

<div class="tagline">We Are the Best Law Firm in Hamilton</div>

<main class="wrap">
  <div class="intro">
    <section class="welcome">
      <h2 class="section-title">Welcome to <span>Brindell Legal</span></h2>
      <div class="welcome-body">
        <div class="portrait" role="img" aria-label="Portrait photo of principal solicitor Ross Kedwick"></div>
        <div class="welcome-text">
          <p>Brindell Legal is a new Hamilton practice offering friendly, personal legal service built on local knowledge. We take time to understand each client and explain every step in plain language. Whether you are buying a home, selling a business or planning your estate, we give clear advice at fair fees and stay with you until the matter is done. Call or visit our office for an obligation free chat about your needs today.</p>
          <span class="read-more">Read More</span>
        </div>
      </div>
    </section>
    <aside class="areas">
      <h2 class="section-title">Areas of <span>Practice</span></h2>
      <ul>
        <li>Commercial Law</li>
        <li>Business Sale and Purchases</li>
        <li>Leases</li>
        <li>Conveyancing and Property Law</li>
        <li>Wills and Estates</li>
        <li>Powers of Attorney</li>
        <li>General Legal Advice</li>
        <li>Succession Planning</li>
      </ul>
    </aside>
  </div>
</main>

<section class="why">
  <svg class="why-notch" width="24" height="12" viewBox="0 0 24 12"><path d="M0 0h24L12 12z" fill="#fff"/></svg>
  <h2>Why Choose Us</h2>
  <p class="lead">We are a local firm that knows Hamilton and the people who live and work here. Our clients deal directly with their solicitor, receive prompt replies and clear costs, and benefit from practical advice shaped around their goals.</p>
  <div class="why-points">
    <ul>
      <li><svg width="10" height="10" viewBox="0 0 10 10"><path d="M1 5l3 3 5-7" fill="none" stroke="#fff" stroke-width="2"/></svg>Personal service from your own solicitor</li>
      <li><svg width="10" height="10" viewBox="0 0 10 10"><path d="M1 5l3 3 5-7" fill="none" stroke="#fff" stroke-width="2"/></svg>Local knowledge of Hamilton and district</li>
      <li><svg width="10" height="10" viewBox="0 0 10 10"><path d="M1 5l3 3 5-7" fill="none" stroke="#fff" stroke-width="2"/></svg>Clear fees agreed before work begins</li>
    </ul>
    <ul>
      <li><svg width="10" height="10" viewBox="0 0 10 10"><path d="M1 5l3 3 5-7" fill="none" stroke="#fff" stroke-width="2"/></svg>Prompt replies to calls and emails</li>
      <li><svg width="10" height="10" viewBox="0 0 10 10"><path d="M1 5l3 3 5-7" fill="none" stroke="#fff" stroke-width="2"/></svg>Plain language advice you can act on</li>
      <li><svg width="10" height="10" viewBox="0 0 10 10"><path d="M1 5l3 3 5-7" fill="none" stroke="#fff" stroke-width="2"/></svg>Trusted by banks and local agents</li>
    </ul>
  </div>
  <span class="read-more">Read More</span>
</section>

<footer class="site-footer">
  <div class="wrap footer-cols">
    <div class="footer-col links">
      <h3>Quick Links</h3>
      <ul>
        <li>Home</li>
        <li>About Us</li>
        <li>Why Choose Us</li>
        <li>Areas of Practice</li>
        <li>Contact Us</li>
      </ul>
    </div>
    <div class="footer-col contact">
      <h3>Contact Details</h3>
      <p>BRINDELL LEGAL</p>
      <p>17 Pellow Road, Hamilton VIC 3300</p>
      <p>Ph: (03) 5598 4731</p>
      <p>Fax: (03) 5598 4706</p>
      <p>ross.kedwick@brindelllegal-example.com.au</p>
    </div>
    <div class="footer-col map">
      <h3>Location Map</h3>
      <div class="map-area" role="img" aria-label="Street map showing the office at 17 Pellow Road, Hamilton"></div>
    </div>
    <div class="footer-col badges">
      <div class="badge guild" role="img" aria-label="Bar Guild of Victoria member badge"></div>
      <div class="badge council" role="img" aria-label="Practitioner oversight Council badge"></div>
    </div>
  </div>
</footer>
<div class="copyright">COPYRIGHT 2013 BRINDELL LEGAL | ALL RIGHTS RESERVED</div>

</body>
</html>
```